Event Graphic for Free Community Event

We need a graphic created for a community event that is aimed at families with younger children called Tots Jamboree. This is a free event and has a fair/carnival feel to it with rides, games, and food. I need the graphic to be flexible enough to be able to be modified and used in a variety of ways on different print and digital marketing materials. I also need the centerpiece of the design to be an event logo that can be used as a standalone element.

The overall feel needs to be fun and friendly with a slightly modern edge to it. Attached are some images used in past events. These are for reference only and do not need to be simulated or used in the final product.

Target Market(s)

Families with children

Industry/Entity Type

Church

Font styles to use
Sans Serif

Requirements
Must have
• - Logo that incorporates the event name
- Event Date: September 19 2020
- Event Time: 10am - 2pm
- Church name and logo incorporated: Bright Harbor Community Church (see attached logo files)
Nice to have
• - Bright colors
- Flexible design elements that are interchangeable and scalable for use of the design in different layouts across different mediums and materials.
Should not have
• - Any references or images related to drugs, alcohol, tobacco, or other subjects that would be inappropriate for children.

```html
<!DOCTYPE html>
<html lang="en">
<head>
<meta charset="utf-8">
<title>Tots Jamboree 2020 – Event Graphic Set</title>
<link rel="stylesheet" href="https://fonts.googleapis.com/css2?family=Nunito:ital,wght@0,400;0,600;0,700;0,800;0,900;1,400&display=swap">
<style>
  :root {
    --ink: #1f1f1f;
    --charcoal: #2b2b2b;
    --paper: #ffffff;
    --teal: #1cc0a8;
    --teal-light: #8de3d8;
    --blue: #1b62d0;
    --sky: #6f9bf0;
    --pink: #ef5873;
    --sun: #f7c35c;
    --sand: #d9d3c8;
    --disc: #ebe9e5;
    --wall: #f1f0ee;
  }
  * { box-sizing: border-box; margin: 0; padding: 0; }
  html, body { width: 983px; height: 1200px; overflow: hidden; background: var(--paper); }
  body { font-family: "Nunito", sans-serif; color: var(--ink); }
  .canvas { position: relative; width: 983px; height: 1200px; overflow: hidden; background: var(--paper); }

  .poster { position: absolute; overflow: hidden; }
  .poster--light { left: 53px; top: 27px; width: 433px; height: 434px; background: var(--paper); border: 1px solid #9a9a9a; }
  .poster--dark { left: 496px; top: 27px; width: 433px; height: 434px; background: var(--charcoal); color: var(--paper); }
  .poster--photo { left: 56px; top: 469px; width: 431px; height: 378px; background: var(--wall); }
  .poster--activities { left: 496px; top: 469px; width: 438px; height: 646px; background: var(--paper); }
  .standalone { position: absolute; left: 0; top: 860px; width: 490px; height: 260px; }

  .variant-tag { position: absolute; right: 0; bottom: 0; height: 13px; padding: 0 6px; background: var(--ink); color: var(--paper); font-size: 6.5px; font-style: italic; line-height: 13px; }
  .poster--dark .variant-tag { background: var(--paper); color: var(--ink); }

  .church { position: absolute; left: 0; right: 0; display: flex; justify-content: center; align-items: center; gap: 4px; }
  .church__mark { width: 32px; height: 32px; border-radius: 50%; background: var(--ink); flex: none; }
  .poster--dark .church__mark { background: var(--paper); }
  .church__name { font-weight: 700; line-height: 1; color: inherit; }
  .church__name span { display: block; }
  .church__name .line1 { font-size: 15px; letter-spacing: 1px; }
  .church__name .line2 { font-size: 7px; letter-spacing: .4px; margin-top: 1px; }

  .present { position: absolute; left: 0; right: 0; text-align: center; font-size: 12px; font-weight: 700; letter-spacing: 1.5px; }

  .event-logo { position: absolute; width: 352px; height: 130px; transform-origin: 0 0; }
  .event-logo__art { position: absolute; left: 30px; top: 30px; width: 320px; height: 96px; border-radius: 48px 56px 44px 52px; background: linear-gradient(95deg, var(--teal) 0%, var(--teal) 30%, var(--pink) 50%, var(--blue) 66%, var(--blue) 100%); border: 2px solid var(--ink); }
  .event-logo__free { position: absolute; left: 8px; top: 4px; width: 118px; height: 36px; border-radius: 22px 26px 24px 6px; background: var(--ink); color: var(--teal); font-size: 21px; font-weight: 900; line-height: 36px; text-align: center; transform: rotate(-12deg); letter-spacing: 1px; }
  .event-logo__name { position: absolute; left: 30px; top: 48px; width: 320px; text-align: center; font-size: 35px; font-weight: 900; color: var(--paper); line-height: 1; letter-spacing: -.5px; }
  .event-logo__year { position: absolute; left: 160px; top: 114px; width: 64px; height: 18px; border-radius: 9px; background: var(--sun); border: 1.5px solid var(--ink); color: var(--ink); font-size: 12px; font-weight: 800; text-align: center; line-height: 15px; letter-spacing: 1px; }

  .event-when { position: absolute; text-align: center; font-weight: 900; line-height: 1.1; }
  .event-when__date { display: block; font-size: 17px; transform: rotate(-2.5deg); }
  .event-when__time { display: block; font-size: 17px; font-weight: 600; margin-top: 1px; }

  .more-info { position: absolute; text-align: center; }
  .more-info__label { display: block; font-size: 8px; font-weight: 700; letter-spacing: .6px; margin-bottom: 4px; }
  .more-info__url { display: inline-block; height: 19px; padding: 0 9px; border-radius: 10px; background: var(--ink); color: var(--paper); font-size: 10.5px; font-weight: 600; line-height: 19px; white-space: nowrap; }
  .poster--dark .more-info__url { background: var(--paper); color: var(--ink); }

  .deco { position: absolute; overflow: visible; }

  .photo-wall { position: absolute; inset: 0; background: linear-gradient(180deg, #f6f5f3 0%, #eeece9 60%, #e7e4df 100%); }
  .photo-kids { position: absolute; left: 14px; right: 14px; top: 250px; height: 128px; border-radius: 40px 40px 0 0; background: linear-gradient(90deg, #d77f96 0%, #c9a38f 20%, #3e4c6e 38%, #e8e4e4 52%, #2f4b79 60%, #59b566 75%, #d4433f 92%); opacity: .85; }

  .activity { position: absolute; z-index: 1; width: 102px; height: 102px; border-radius: 50%; background: var(--disc); border: 3px solid var(--ink); }
  .activity__label { position: absolute; z-index: 2; width: 120px; text-align: center; font-size: 12.5px; font-weight: 900; letter-spacing: .5px; line-height: 1; white-space: nowrap; transform: translateX(-50%); }
</style>
</head>
<body>
<main class="canvas">

  <!-- Light background version -->
  <section class="poster poster--light">
    <div class="church" style="top:50px"><span class="church__mark"></span><p class="church__name"><span class="line1">BRIGHT HARBOR</span><span class="line2">COMMUNITY CHURCH</span></p></div>
    <p class="present" style="top:88px">PRESENT</p>
    <div class="event-logo" style="left:33px;top:125px">
      <div class="event-logo__art" role="img" aria-label="Scribbled teal, pink and blue blob artwork with paper plane and sun doodles"></div>
      <p class="event-logo__free">FREE!</p>
      <p class="event-logo__name">TOTS JAMBOREE</p>
      <p class="event-logo__year">2020</p>
    </div>
    <p class="event-when" style="left:60px;width:300px;top:262px"><span class="event-when__date">SATURDAY SEPTEMBER 19 2020</span><span class="event-when__time">10AM - 2PM</span></p>
    <p class="more-info" style="left:100px;width:246px;top:342px"><span class="more-info__label">More Information</span><span class="more-info__url">brightharborchurch.org/jamboree</span></p>
    <svg class="deco" style="left:377px;top:36px" width="20" height="20"><polygon fill="#ef5873" points="10,0 12.9,6.9 20,7.6 14.6,12.2 16.2,19.5 10,15.6 3.8,19.5 5.4,12.2 0,7.6 7.1,6.9"/></svg>
    <svg class="deco" style="left:46px;top:58px" width="28" height="28"><circle cx="14" cy="14" r="11" fill="none" stroke="#6f9bf0" stroke-width="3"/></svg>
    <svg class="deco" style="left:316px;top:304px" width="16" height="18"><polygon fill="#ef5873" points="0,0 16,9 2,18"/></svg>
    <svg class="deco" style="left:366px;top:348px" width="14" height="14"><polygon fill="#f7c35c" points="7,0 9,5 14,5.3 10.2,8.5 11.3,13.6 7,10.9 2.7,13.6 3.8,8.5 0,5.3 5,5"/></svg>
    <svg class="deco" style="left:38px;top:370px" width="38" height="38"><polyline fill="none" stroke="#1cc0a8" stroke-width="3.5" points="2,36 2,28 10,28 10,20 18,20 18,12 26,12 26,4 36,2"/></svg>
    <p class="variant-tag">For bright background</p>
  </section>

  <!-- Dark background version -->
  <section class="poster poster--dark">
    <div class="church" style="top:50px"><span class="church__mark"></span><p class="church__name"><span class="line1">BRIGHT HARBOR</span><span class="line2">COMMUNITY CHURCH</span></p></div>
    <p class="present" style="top:88px">PRESENT</p>
    <div class="event-logo" style="left:33px;top:125px">
      <div class="event-logo__art" role="img" aria-label="Scribbled teal, pink and blue blob artwork with paper plane and sun doodles"></div>
      <p class="event-logo__free">FREE!</p>
      <p class="event-logo__name">TOTS JAMBOREE</p>
      <p class="event-logo__year">2020</p>
    </div>
    <p class="event-when" style="left:60px;width:300px;top:262px"><span class="event-when__date">SATURDAY SEPTEMBER 19 2020</span><span class="event-when__time">10AM - 2PM</span></p>
    <p class="more-info" style="left:100px;width:246px;top:342px"><span class="more-info__label">More Information</span><span class="more-info__url">brightharborchurch.org/jamboree</span></p>
    <svg class="deco" style="left:377px;top:36px" width="20" height="20"><polygon fill="#ef5873" points="10,0 12.9,6.9 20,7.6 14.6,12.2 16.2,19.5 10,15.6 3.8,19.5 5.4,12.2 0,7.6 7.1,6.9"/></svg>
    <svg class="deco" style="left:46px;top:58px" width="28" height="28"><circle cx="14" cy="14" r="11" fill="none" stroke="#6f9bf0" stroke-width="3"/></svg>
    <svg class="deco" style="left:316px;top:304px" width="16" height="18"><polygon fill="#ef5873" points="0,0 16,9 2,18"/></svg>
    <svg class="deco" style="left:366px;top:348px" width="14" height="14"><polygon fill="#f7c35c" points="7,0 9,5 14,5.3 10.2,8.5 11.3,13.6 7,10.9 2.7,13.6 3.8,8.5 0,5.3 5,5"/></svg>
    <svg class="deco" style="left:38px;top:370px" width="38" height="38"><polyline fill="none" stroke="#ffffff" stroke-width="3.5" points="2,36 2,28 10,28 10,20 18,20 18,12 26,12 26,4 36,2"/></svg>
    <p class="variant-tag">For dark background</p>
  </section>

  <!-- Photo version -->
  <section class="poster poster--photo">
    <div class="photo-wall" role="img" aria-label="White painted brick wall backdrop"></div>
    <div class="photo-kids" role="img" aria-label="Row of young children in colourful clothes pointing upward"></div>
    <svg class="deco" style="left:0;top:334px" width="431" height="44" viewBox="0 0 431 44" preserveAspectRatio="none"><path fill="#1b62d0" d="M0,10 C40,0 80,10 120,30 L120,44 L0,44 Z M330,30 C370,14 400,6 431,2 L431,44 L330,44 Z"/><path fill="#f7c35c" d="M60,44 C100,20 150,6 210,14 C260,20 300,30 360,36 L380,44 Z"/></svg>
    <div class="church" style="top:12px"><span class="church__mark" style="width:24px;height:24px"></span><p class="church__name"><span class="line1" style="font-size:12px">BRIGHT HARBOR</span><span class="line2" style="font-size:5.5px">COMMUNITY CHURCH</span></p></div>
    <div class="event-logo" style="left:56px;top:44px;transform:scale(.9)">
      <div class="event-logo__art" role="img" aria-label="Scribbled teal, pink and blue blob artwork with paper plane and sun doodles"></div>
      <p class="event-logo__free">FREE!</p>
      <p class="event-logo__name">TOTS JAMBOREE</p>
      <p class="event-logo__year">2020</p>
    </div>
    <p class="event-when" style="left:66px;width:290px;top:170px"><span class="event-when__date" style="font-size:16px">SATURDAY SEPTEMBER 19 2020</span><span class="event-when__time" style="font-size:16px">10AM - 2PM</span></p>
    <p class="more-info" style="left:90px;width:250px;top:211px"><span class="more-info__label" style="font-size:7px;margin-bottom:2px">More Information</span><span class="more-info__url" style="font-size:10px">brightharborchurch.org/jamboree</span></p>
    <svg class="deco" style="left:350px;top:13px" width="18" height="18"><polygon fill="#ef5873" points="9,0 11.6,6.2 18,6.8 13.1,11 14.6,17.5 9,14 3.4,17.5 4.9,11 0,6.8 6.4,6.2"/></svg>
    <svg class="deco" style="left:22px;top:26px" width="26" height="26"><circle cx="13" cy="13" r="10" fill="none" stroke="#6f9bf0" stroke-width="3"/></svg>
    <svg class="deco" style="left:314px;top:212px" width="15" height="16"><polygon fill="#ef5873" points="0,0 15,9 2,16"/></svg>
    <svg class="deco" style="left:383px;top:230px" width="12" height="12"><polygon fill="#f7c35c" points="6,0 7.7,4.3 12,4.5 8.7,7.3 9.7,11.6 6,9.3 2.3,11.6 3.3,7.3 0,4.5 4.3,4.3"/></svg>
    <svg class="deco" style="left:25px;top:210px" width="36" height="26"><polyline fill="none" stroke="#1cc0a8" stroke-width="3.5" points="1,24 9,16 13,22 21,12 25,18 35,4"/></svg>
  </section>

  <!-- Activities version -->
  <section class="poster poster--activities">
    <svg class="deco" style="left:0;top:0" width="438" height="44" viewBox="0 0 438 44" preserveAspectRatio="none"><path fill="#f7c35c" d="M60,0 L438,0 L438,22 C390,36 350,10 300,16 C250,22 220,40 180,36 C140,32 110,10 60,0 Z"/><path fill="#1b62d0" d="M0,0 L110,0 C80,12 50,24 30,30 C15,34 5,36 0,38 Z M340,0 L438,0 L438,30 C410,28 380,10 340,0 Z"/></svg>
    <div class="church" style="top:24px"><span class="church__mark" style="width:30px;height:30px"></span><p class="church__name"><span class="line1">BRIGHT HARBOR</span><span class="line2">COMMUNITY CHURCH</span></p></div>
    <p class="present" style="top:82px">PRESENT</p>
    <div class="event-logo" style="left:44px;top:100px;transform:scale(.99)">
      <div class="event-logo__art" role="img" aria-label="Scribbled teal, pink and blue blob artwork with paper plane and sun doodles"></div>
      <p class="event-logo__free">FREE!</p>
      <p class="event-logo__name">TOTS JAMBOREE</p>
      <p class="event-logo__year">2020</p>
    </div>
    <p class="event-when" style="left:68px;width:306px;top:234px"><span class="event-when__date">SATURDAY SEPTEMBER 19 2020</span><span class="event-when__time">10AM - 2PM</span></p>

    <div class="activity" style="left:73px;top:312px"></div>
    <div class="activity" style="left:280px;top:312px"></div>
    <div class="activity" style="left:108px;top:386px"></div>
    <div class="activity" style="left:244px;top:386px"></div>
    <div class="activity" style="left:177px;top:336px"></div>

    <p class="activity__label" style="left:124px;top:292px;transform:translateX(-50%) rotate(-10deg)">BUNGEE JUMP</p>
    <p class="activity__label" style="left:228px;top:286px">FOOD</p>
    <p class="activity__label" style="left:228px;top:318px">FOOD</p>
    <p class="activity__label" style="left:331px;top:292px;transform:translateX(-50%) rotate(9deg)">ROCK WALL</p>
    <p class="activity__label" style="left:159px;top:492px">RIDES</p>
    <p class="activity__label" style="left:295px;top:490px;transform:translateX(-50%) rotate(-4deg)">INFLATABLES</p>

    <p class="more-info" style="left:100px;width:250px;top:536px"><span class="more-info__label">More Information</span><span class="more-info__url">brightharborchurch.org/jamboree</span></p>

    <svg class="deco" style="left:0;top:560px" width="438" height="86" viewBox="0 0 438 86" preserveAspectRatio="none"><path fill="#1cc0a8" d="M0,18 C30,10 50,20 70,30 L70,86 L0,86 Z M300,86 C330,60 380,40 438,0 L438,86 Z"/><path fill="#8de3d8" d="M90,40 C160,30 220,20 280,24 C330,28 370,40 400,60 L400,86 L90,86 Z"/><path fill="#d9d3c8" d="M40,28 C80,20 120,36 160,50 C200,64 260,70 300,86 L60,86 Z"/><path fill="#1cc0a8" d="M0,40 C40,46 80,60 170,86 L0,86 Z"/></svg>
    <svg class="deco" style="left:23px;top:264px" width="24" height="24"><circle cx="12" cy="12" r="9" fill="none" stroke="#f7c35c" stroke-width="3"/></svg>
    <svg class="deco" style="left:375px;top:80px" width="14" height="14"><polygon fill="#ef5873" points="7,0 9,5 14,5.3 10.2,8.5 11.3,13.6 7,10.9 2.7,13.6 3.8,8.5 0,5.3 5,5"/></svg>
    <svg class="deco" style="left:46px;top:276px" width="14" height="14"><polygon fill="#6f9bf0" points="7,0 9,5 14,5.3 10.2,8.5 11.3,13.6 7,10.9 2.7,13.6 3.8,8.5 0,5.3 5,5"/></svg>
    <svg class="deco" style="left:389px;top:416px" width="14" height="14"><polygon fill="#6f9bf0" points="7,0 9,5 14,5.3 10.2,8.5 11.3,13.6 7,10.9 2.7,13.6 3.8,8.5 0,5.3 5,5"/></svg>
    <svg class="deco" style="left:364px;top:542px" width="16" height="18"><polygon fill="#ef5873" points="0,0 16,9 2,18"/></svg>
    <svg class="deco" style="left:34px;top:425px" width="30" height="30"><polyline fill="none" stroke="#1cc0a8" stroke-width="3" points="2,28 2,22 9,22 9,15 16,15 16,8 23,8 23,2 28,2"/></svg>
  </section>

  <!-- Standalone event logo -->
  <section class="standalone">
    <div class="event-logo" style="left:76px;top:42px;transform:scale(1.04)">
      <div class="event-logo__art" role="img" aria-label="Scribbled teal, pink and blue blob artwork with paper plane and sun doodles"></div>
      <p class="event-logo__free">FREE!</p>
      <p class="event-logo__name">TOTS JAMBOREE</p>
      <p class="event-logo__year">2020</p>
    </div>
    <p class="event-when" style="left:112px;width:310px;top:194px"><span class="event-when__date">SATURDAY SEPTEMBER 19 2020</span><span class="event-when__time">10AM - 2PM</span></p>
  </section>

</main>
</body>
</html>
```